Tobin's Harbor Table Restaurant and Bar

Tobin's Harbor Table is a casual dining restaurant and bar experience. We are owned by Gregory (originally from Chicago), and Lorna (originally from Tucson, Arizona). Gregory and Lorna spent much of their lives traveling and working around the world and have landed in Boquete, Chiriqui, Republic of Panama, where they own Tobin's Harbor Table, a popular, casual dining restaurant and watering hole. Tobin's has been here for over four years, and is in desperate need of a website makeover.

Our website should be easy to maintain, clean look and represent our brand, and our logo. We need to easily maintain the content as we have constant new events, holidays, sponsorships, sports, live music, etc.

We live in the agricultural hub of Central American, and we dedicated to all our ingredients being local, however, used in dishes that represent all corners of the globe. Some of our favorites are our Orange Chicken, Pad Thai, North Carolina Pulled Pork.

We also have the largest beer selection in all of panama with three local microbrews and beers and wines from every corner of the globe, ncluding a growing collection of American Microbrews . . . We also have the best whiskey selection including American, Irish, Scottish, Canadian, randing from $2 to $50 a shot . . .

We take pride in great food in a "divey" atmosphere . . .

www.tobinsharbortable.example
Boquete, Chiriqui, Republic of Panama

Also, We want the website to direct to another website for special events and such, something easy to maintain or that is imbedded into site, we want the site to be static, but current, where social media will serve as a way to discuss what changes day-to-day more than the website.
Updates

Our webpage is a good reference, but hard and cumbersome to update, make it easy and simple, clean and modern looking. Check our facebook page at Tobin's Harbor Table in Boquete for more up-to-date information. Greg

Target Market(s)

Tourists, Panamanian Customers, Expatriates, and other Locals. Sports and Live Music fans.

Industry/Entity Type

Restaurant

Number of Pages Required

1 page

Font styles to use
Other font styles liked:
• Please see our logo, and compliment or parallel as appropriate

Requirements
Must have
• Links to my menus or menus easily embedded into the site, I can provide links or pdf or jpg files of menus.
Nice to have
• Ability to switch between a Spanish and English version (I can have the website translated, but there should be two sides of the site, links to voyagerate, and social media.

```html
<!DOCTYPE html>
<html lang="en">
<head>
<meta charset="utf-8">
<title>Tobin's Harbor Table</title>
<link href="https://fonts.googleapis.com/css2?family=Crimson+Text:ital,wght@0,400;0,600;0,700;1,400&family=Great+Vibes&display=swap" rel="stylesheet">
<style>
:root{
  --green:#3f9a3a;
  --green-dark:#2e7a2b;
  --ink:#222;
  --text:#444;
  --muted:#888;
  --line:#d8d8d8;
  --dark:#1d1d1d;
  --footer:#2a2a2a;
  --paper:#ffffff;
  --soft:#f3f3f3;
}
*{box-sizing:border-box;margin:0;padding:0}
html,body{width:1200px;height:2876px;overflow:hidden;background:var(--paper)}
body{font-family:"Crimson Text",Georgia,serif;color:var(--text)}
a{color:inherit;text-decoration:none}

.site-header{height:232px;position:relative}
.brand{position:absolute;left:0;right:0;top:38px;text-align:center}
.brand-name{font-size:40px;font-weight:600;color:var(--green);line-height:1}
.brand-tagline{font-size:15px;color:var(--ink);margin-top:8px;letter-spacing:.5px}
.lang-switch{position:absolute;right:48px;top:34px;font-size:19px;font-weight:600}
.lang-switch .active{color:var(--green)}
.main-nav{position:absolute;left:48px;right:48px;top:152px;display:flex;justify-content:space-between;font-size:21px;font-weight:600;color:var(--ink)}

.hero{position:relative;margin:0 48px;height:548px;background:radial-gradient(ellipse at 50% 45%,#c46a3a 0%,#7a3b22 30%,#2b1a14 65%,#111 100%)}
.hero-caption{position:absolute;left:0;right:0;top:262px;text-align:center;color:#fff}
.hero-caption h1{font-family:"Great Vibes",cursive;font-weight:400;font-size:62px;line-height:1}
.hero-caption p{font-size:18px;letter-spacing:2px;text-transform:uppercase;margin-top:4px}
.hero-arrow{position:absolute;top:272px;width:40px;height:40px}
.hero-arrow.prev{left:12px}.hero-arrow.next{right:12px}

.intro{display:flex;margin:0 48px;height:480px;padding-top:4px}
.menus{width:256px;padding-top:30px}
.menus h2{font-size:34px;color:var(--ink);line-height:1.05;font-weight:700;border-bottom:3px solid var(--ink);padding-bottom:12px}
.menus ul{list-style:none;margin-top:18px}
.menus li{border:2px solid var(--ink);font-size:17px;font-weight:600;color:var(--ink);padding:12px 14px;margin-bottom:14px;text-align:center}
.restaurant{flex:1;text-align:center;padding:30px 36px 0}
.restaurant h2{font-size:34px;color:var(--ink);font-weight:700}
.restaurant .sub{font-size:16px;color:var(--ink);margin:2px 0 14px}
.restaurant p{font-size:16px;line-height:1.45}
.chef{margin-top:22px;display:flex;flex-direction:column;align-items:center}
.chef-photo{width:64px;height:64px;border-radius:50%;background:linear-gradient(#9c9c9c,#5c5c5c);border:3px solid var(--green)}
.chef-name{font-size:17px;color:var(--ink);margin-top:8px;border-top:1px solid var(--line);padding-top:6px;width:180px}
.aside{width:296px;padding-top:30px}
.event{background:var(--dark);color:#fff;text-align:center;padding:0 0 22px;height:196px}
.event-tag{display:inline-block;background:var(--green);font-size:21px;font-weight:600;padding:6px 20px;margin:14px 0 10px;margin-left:-40px}
.event h3{font-size:21px;font-weight:600}
.event p{font-size:14px;line-height:1.4;color:#ddd}
.award{margin:28px auto 0;width:240px;text-align:center}
.award-badge{width:96px;height:96px;margin:0 auto;border-radius:50%;background:#e6e6e6;border:4px solid var(--green)}
.award-bar{background:var(--green);color:#fff;font-size:18px;font-weight:700;padding:6px;margin-top:10px}

.specials{position:relative;height:660px;background:linear-gradient(180deg,#2a2522 0%,#4a3c33 40%,#2d2622 75%,#1a1614 100%)}
.specials h2{position:absolute;left:0;right:0;top:50px;text-align:center;font-family:"Great Vibes",cursive;font-weight:400;color:#fff;font-size:64px}
.dish-list{position:absolute;left:56px;right:56px;top:220px;display:flex;justify-content:space-between}
.dish{width:256px;text-align:center;color:#fff}
.dish-photo{height:170px;border:4px solid #fff}
.dish-name{background:rgba(0,0,0,.6);font-size:19px;padding:10px 0 2px}
.dish-price{background:rgba(0,0,0,.6);font-size:15px;padding-bottom:10px}

.social-row{display:flex;margin:0 48px;height:460px;padding-top:52px}
.testimonials{flex:1;text-align:center;padding-right:60px}
.section-title{font-size:34px;font-weight:700;color:var(--ink);letter-spacing:1px;line-height:1}
.section-sub{font-size:17px;color:var(--green);margin-top:4px}
.quote-mark{font-size:90px;line-height:.8;color:var(--ink);margin-top:24px;height:52px}
.testimonials p{font-size:17px;line-height:1.45;margin-top:8px;padding:0 30px}
.guest{font-size:18px;font-weight:700;color:var(--ink);margin-top:12px}
.guest-date{font-size:14px;color:var(--muted)}
.feed{width:440px;text-align:center}
.feed-icon{width:34px;height:34px;border-radius:50%;background:var(--ink);margin:14px auto 16px}
.feed p{font-size:17px;line-height:1.45;color:var(--ink)}
.feed .link{color:var(--green)}
.feed-meta{display:flex;justify-content:space-between;align-items:center;margin-top:16px;font-size:15px;color:var(--green)}
.feed-actions{display:flex;gap:14px}
.dots{display:flex;gap:8px;justify-content:center;margin-top:26px}
.dots span{width:14px;height:14px;border-radius:50%;background:var(--line)}
.dots span.on{background:var(--ink)}

.visit{display:flex;margin:0 48px;height:380px}
.gallery{position:relative;width:600px;display:grid;grid-template-columns:1fr 1fr 1fr;grid-template-rows:1fr 1fr;gap:4px}
.gallery div{background:linear-gradient(135deg,#6b5646,#2e2520)}
.gallery div:nth-child(2){background:linear-gradient(135deg,#8a6a4a,#3a2e24)}
.gallery div:nth-child(4){background:linear-gradient(135deg,#3a3a3a,#151515)}
.gallery div:nth-child(5){background:linear-gradient(135deg,#9a7d5d,#4a3a2a)}
.gallery-label{position:absolute;left:205px;top:150px;width:190px;height:80px;background:rgba(0,0,0,.6);color:#fff;font-size:34px;font-weight:600;display:flex;align-items:center;justify-content:center}
.location{flex:1;position:relative;background:linear-gradient(135deg,#c9c6bd,#b1aea5 50%,#d4d1c9);text-align:center;color:#fff;padding-top:98px}
.location::before{content:"";position:absolute;inset:0;background:rgba(40,40,40,.45)}
.location > *{position:relative}
.location h3{font-size:30px;font-weight:600}
.location .address{font-size:18px;margin-top:6px}
.map-btn{display:inline-block;border:2px solid #fff;font-size:17px;padding:8px 22px;margin-top:26px}

.site-footer{position:absolute;left:0;right:0;top:2784px}
.footer-row{display:flex;justify-content:space-between;align-items:center;margin:0 48px;height:40px}
.footer-nav{display:flex;gap:24px;font-size:20px;color:var(--ink)}
.footer-social{display:flex;gap:10px}
.footer-social span{width:28px;height:28px;border-radius:50%;background:var(--ink)}
.copyright{background:var(--footer);color:#ccc;font-size:12px;text-align:center;height:52px;line-height:52px;margin-top:0}
</style>
</head>
<body>
<header class="site-header">
  <div class="brand">
    <div class="brand-name">Tobin's Harbor Table</div>
    <div class="brand-tagline">Boquete, Chiriqui, Republic of Panama</div>
  </div>
  <div class="lang-switch"><a href="#" class="active">Spanish</a> | <a href="#">English</a></div>
  <nav class="main-nav">
    <a href="#">Home</a><a href="#">About</a><a href="#">Contact</a><a href="#">Social Media</a><a href="#">Find Us</a><a href="#">Gallery</a><a href="#">Menu</a><a href="#">Events</a>
  </nav>
</header>

<section class="hero" role="img" aria-label="Plated signature dish on a restaurant table">
  <svg class="hero-arrow prev" viewBox="0 0 40 40"><circle cx="20" cy="20" r="18" fill="#fff"/><path d="M23 12l-8 8 8 8" stroke="#222" stroke-width="3" fill="none"/></svg>
  <div class="hero-caption">
    <h1>Tobin's Harbor Table</h1>
    <p>Boquete Chiriqui Republic of Panama</p>
  </div>
  <svg class="hero-arrow next" viewBox="0 0 40 40"><circle cx="20" cy="20" r="18" fill="#fff"/><path d="M17 12l8 8-8 8" stroke="#222" stroke-width="3" fill="none"/></svg>
</section>

<section class="intro">
  <div class="menus">
    <h2>Today's<br>Menus</h2>
    <ul>
      <li>Breakfast</li>
      <li>Children's Menu</li>
      <li>Beverage</li>
      <li>Lunch and Dinner Menu</li>
    </ul>
  </div>
  <div class="restaurant">
    <h2>Restaurant</h2>
    <div class="sub">Welcome to Tobin's Harbor Table</div>
    <p>Local ingredients from the Chiriqui highlands, cooked into dishes from every corner of the globe. Pull up a stool, order a local microbrew or a whiskey from our shelf, and settle into our easy, divey dining room. From Orange Chicken to Pad Thai and North Carolina Pulled Pork, there is a plate here for every traveler and neighbor in Boquete.</p>
    <div class="chef">
      <div class="chef-photo" role="img" aria-label="Portrait of the chef"></div>
      <div class="chef-name">Greg, Chef cook</div>
    </div>
  </div>
  <div class="aside">
    <div class="event">
      <div class="event-tag">Up Coming Event</div>
      <h3>Danny Rowe Live</h3>
      <p>Friday, July 24th 7:00 PM<br>Birthday bash concert on our stage<br>Bring friends and your dancing shoes</p>
    </div>
    <div class="award">
      <div class="award-badge" role="img" aria-label="voyagerate award badge"></div>
      <div class="award-bar">2014 WINNER</div>
    </div>
  </div>
</section>

<section class="specials" role="img" aria-label="Chef preparing a dish in a dark kitchen">
  <h2>Chef's Special</h2>
  <div class="dish-list">
    <div class="dish"><div class="dish-photo" style="background:linear-gradient(135deg,#c9a35c,#7a5a2a)" role="img" aria-label="Falafel plate"></div><div class="dish-name">Falafel Plate</div><div class="dish-price">$12.00</div></div>
    <div class="dish"><div class="dish-photo" style="background:linear-gradient(135deg,#b7874e,#5a3a1e)" role="img" aria-label="Pulled pork sandwiches"></div><div class="dish-name">Pulled Pork Sandwich</div><div class="dish-price">$13.00</div></div>
    <div class="dish"><div class="dish-photo" style="background:linear-gradient(135deg,#c06a2a,#5a2a12)" role="img" aria-label="Orange chicken"></div><div class="dish-name">Orange Chicken</div><div class="dish-price">$7.00</div></div>
    <div class="dish"><div class="dish-photo" style="background:linear-gradient(135deg,#8c6a4a,#3a2818)" role="img" aria-label="Wood-fired chicken"></div><div class="dish-name">Pollo a la Leña</div><div class="dish-price">$9.00</div></div>
  </div>
</section>

<section class="social-row">
  <div class="testimonials">
    <div class="section-title">TESTIMONIALS FROM OUR</div>
    <div class="section-sub">Customers &amp; Friends</div>
    <div class="quote-mark">&ldquo;</div>
    <p>Great food, cold beer and the friendliest crowd in Boquete. We came for one dinner and ended up back three nights in a row for the music and the whiskey list.</p>
    <div class="guest">Marisol</div>
    <div class="guest-date">03.05.2013</div>
  </div>
  <div class="feed">
    <div class="section-title">FOLLOW &nbsp;ON CHIRPER</div>
    <div class="feed-icon"></div>
    <p>Don't miss Danny Rowe's Birthday Bash Concert! 7pm Friday July 24th<br>Where the bar becomes a stage! <span class="link">hrb.tl/24x6Wewb</span></p>
    <div class="feed-meta">
      <span>yesterday</span>
      <span class="feed-actions">
        <svg width="16" height="14" viewBox="0 0 16 14"><path d="M6 1L1 6l5 5V8c4 0 7 1 9 5 0-5-3-8-9-8z" fill="#444"/></svg>
        <svg width="16" height="14" viewBox="0 0 16 14"><path d="M3 3h8v3l3-4-3-4v3H1v5h2zM13 11H5V8l-3 4 3 4v-3h10V8h-2z" fill="#444" transform="translate(0,-1) scale(1,.9)"/></svg>
        <svg width="14" height="14" viewBox="0 0 14 14"><path d="M7 1l1.8 4 4.2.4-3.2 2.8 1 4.2L7 10.2 3.2 12.4l1-4.2L1 5.4l4.2-.4z" fill="#444"/></svg>
      </span>
    </div>
    <div class="dots"><span class="on"></span><span></span><span></span><span></span><span></span></div>
  </div>
</section>

<section class="visit">
  <div class="gallery" role="img" aria-label="Collage of restaurant, bar and live music photos">
    <div></div><div></div><div></div><div></div><div></div><div></div>
    <span class="gallery-label">Gallery</span>
  </div>
  <div class="location" role="img" aria-label="Street map of Bajo Boquete">
    <h3>Restaurant Location</h3>
    <div class="address">Calle Los Robles, Bajo Boquete, Panama</div>
    <a href="#" class="map-btn">See Location on Map</a>
  </div>
</section>

<footer class="site-footer">
  <div class="footer-row">
    <nav class="footer-nav"><a href="#">Home</a><a href="#">About</a><a href="#">Contact</a><a href="#">Social Media</a><a href="#">Find Us</a><a href="#">Gallery</a><a href="#">Menu</a><a href="#">Events</a></nav>
    <div class="footer-social"><span></span><span></span><span></span></div>
  </div>
  <div class="copyright">Copyright &copy; Tobin's Harbor Table. All Rights Reserved</div>
</footer>
</body>
</html>
```